Web Design Project for Recipe Search site

Background
Stir Your Shelves is an internationally (English speaking) focussed website and search engine for cookbooks and recipes for people who love to use great recipes. SYS is a unique way to find recipes from ALL sources – both print and digital. SYS is the ONLY website that indexes print cookbooks and magazines so a member can easily create a searchable bookshelf of ALL their recipe collection regardless of source. Stir Your Shelves provides a way to find recipes from any source - it does not provide the complete recipe. You either use the print source - or there is a link if it is available online.
Recently StirYourShelves created a new home page with a fresh and contemporary design and copy that better captured the essence of the site for potential users. This has improved conversion to membership from that landing page HOWEVER;
The overwhelming majority (60%) of first time visitors to the SYS site land on a Library recipe page while they have been searching for a particular recipe. For most this is their first exposure to SYS and so they come from a basis of little or no knowledge of the site.

THE BRIEF
Design a page that will be a Pop Up box that appears as a visitor arrives on the Library recipe page Use this link for the page example:
http://www.stiryourshelves.example/library/recipes/4827316/baked-spiced-apple-wedges-with

AND
Design a modification to the box (currently blue) that is part of the Library recipe page.
The Library recipe page is part of the overall site design and the overall design cannot be changed until a responsive design upgrade is underway. This will be the next project.

Objective
Increase the capture and engagement for SYS
Increase the visual impact and Brand Identity for SYS
Reduce page bounce and increase conversion into sign on funnel.

Target Market(s)

People who love cooking with great recipes
Our core target is female (70%), aged in her 40s who owns between 40 and 300 cookbooks. She lives in USA, Australia or UK. She loves cookbooks and organization and LOVES cooking great recipes. The reason she loves StirYourShelves is because she can actually use her cookbooks. We have spoken to thousands of people and these quotes reflect the most frequent feedback about why she love Stir Your Shelves.
“Stir Your Shelves is the most exciting thing I’ve found on the internet in ages.”
“It never lets me down when I can’t remember which of my 13 Colin Hartwell books a recipe is in.

Industry/Entity Type

Digital

Number of Pages Required

1 page

Requirements
Must have
• Consistent with Home Page - fresh, clean, contemporary, approachable, culinary
• http://www.stiryourshelves.example/
• Use fonts consistent with existing page - see Style Guide attached.
• http://www.stiryourshelves.example/library/recipes/4827316/baked-spiced-apple-wedges-with
Nice to have
• Suggested Copy for Pop Up Box
• REDISCOVER YOUR cookbooks
• Join a community of cookbook lovers & discover that Stir Your Shelves is a great way to make better use of your own collection
• Find any recipe from your own recipe collection in seconds
• Stir Your Shelves has indexed over 1 million recipes – so now you can have a search engine to find all your recipes in your cookbooks, magazines & favorite blogs
• Connect with a community of like-minded enthusiasts
• Exchange recommendations with other members, discover new ideas & read blogs written by culinary enthusiasts
• Become a member and start organizing your recipes.
• Suggested New copy for Library recipe page
• If this recipe is available online – click on the link “View complete recipe” below
• SYS is a recipe search engine for your personal collection. If there’s no link, it means you need to own the book or magazine to see the complete recipe.
• Find out more. (button)
• Join now and get started (button)
Should not have
• Use any new fonts or colors. Stick to colors on site.

```html
<!DOCTYPE html>
<html lang="en">
<head>
<meta charset="utf-8">
<title>Stir Your Shelves – Rediscover Your Cookbooks</title>
<link rel="stylesheet" href="https://fonts.googleapis.com/css2?family=Raleway:wght@300;400;500;600&family=Open+Sans:ital,wght@0,400;0,600;1,400&family=Great+Vibes&display=swap">
<style>
:root{
  --brand-green:#6ab23a;
  --section-green:#3b7a1f;
  --hero-panel:rgba(74,150,40,.88);
  --accent:#c5603a;
  --ink:#222;
  --ink-soft:#444;
  --dark-band:#2e2e2e;
  --footer-bg:#f7f7f7;
  --rule:#e2e2e2;
  --white:#fff;
  --social:#1f6fb0;
}
*{box-sizing:border-box;margin:0;padding:0}
html,body{width:1200px;height:2247px;overflow:hidden;background:var(--white)}
body{font-family:"Open Sans",Arial,sans-serif;color:var(--ink);position:relative}
.heading{font-family:"Raleway",Arial,sans-serif}

/* Header */
.site-header{height:96px;position:relative;border-bottom:1px solid var(--rule)}
.brand{position:absolute;left:150px;top:26px;display:flex;align-items:center;gap:10px}
.brand-mark{width:22px;height:22px;background:var(--brand-green);border-radius:50%}
.brand-name{font-family:"Raleway",sans-serif;font-size:19px;font-weight:500;color:var(--ink-soft)}
.member-link{position:absolute;left:845px;top:41px;font-size:15px;color:var(--ink)}
.login-btn{position:absolute;left:976px;top:37px;width:76px;height:30px;background:var(--accent);color:var(--white);font-size:15px;text-align:center;line-height:30px;border-radius:2px}

/* Hero */
.hero{height:558px;position:relative;overflow:hidden}
.hero-photo{position:absolute;inset:0;background:linear-gradient(90deg,#1a1a1a 0%,#6e6a66 25%,#d9d6d2 50%,#8d8a84 75%,#1c1c1c 100%)}
.hero-panel{position:absolute;left:347px;top:160px;width:535px;height:199px;background:var(--hero-panel);border:1px solid rgba(255,255,255,.6);text-align:center;color:var(--white)}
.hero-kicker{margin-top:24px;font-size:19px;font-weight:500;letter-spacing:.5px;color:#1e2a12}
.hero-script{font-family:"Great Vibes",cursive;font-size:78px;line-height:72px;margin-top:2px}
.hero-lead{font-size:14.5px;line-height:20px;margin-top:10px;padding:0 40px}
.slider-arrow{position:absolute;top:223px}

/* Features */
.features{height:392px;position:relative}
.feature{position:absolute;top:39px;width:400px;text-align:center}
.feature--search{left:193px}
.feature--community{left:620px}
.feature-photo{width:166px;height:166px;border-radius:50%;margin:0 auto}
.feature--search .feature-photo{background:radial-gradient(circle at 40% 40%,#f4f4f4,#c9c9c9 70%,#e38a3a)}
.feature--community .feature-photo{background:radial-gradient(circle at 50% 50%,#7cab4a,#c8a77a 60%,#8a6a44)}
.feature-title{font-size:20px;margin-top:11px;color:var(--ink)}
.feature-sub{font-size:26px;margin-top:3px;color:var(--ink)}
.feature-text{font-size:12.5px;line-height:21px;margin-top:10px;color:var(--ink)}

/* Join band */
.join-band{height:232px;position:relative;overflow:hidden;text-align:center;color:var(--white)}
.join-photo{position:absolute;inset:0;background:linear-gradient(90deg,#2a2a2a 0%,#58504a 30%,#6a625a 55%,#3a3a3a 90%,#2a2a2a 100%)}
.join-content{position:relative}
.join-title{font-size:37px;font-weight:400;margin-top:58px;letter-spacing:.5px}
.join-sub{font-size:25px;font-weight:400;margin-top:2px}
.read-more{display:inline-block;margin-top:14px;width:96px;height:27px;line-height:27px;background:#3e8a22;font-size:11px;font-weight:600;border-radius:2px}

/* Library box */
.library{height:390px;background:var(--section-green);position:relative;color:var(--white)}
.library-copy{position:absolute;left:146px;top:99px;width:540px}
.library-title{font-size:27px;font-weight:300}
.library-sub{font-size:18px;line-height:22px;margin-top:12px}
.library-text{font-size:12.5px;line-height:21px;margin-top:14px}
.library-actions{display:flex;gap:7px;margin-top:17px}
.btn{height:31px;line-height:31px;font-size:13px;text-align:center;border-radius:2px;color:var(--white)}
.btn--primary{background:var(--accent);width:115px}
.btn--dark{background:#222;width:173px}
.library-photo{position:absolute;left:723px;top:85px;width:333px;height:215px;background:linear-gradient(135deg,#9a8b7a,#c26a2a 45%,#3c4a2a 80%,#d8d3cc)}

/* Testimonials */
.testimonials{height:265px;position:relative;text-align:center}
.testimonials-title{font-size:27px;font-weight:400;padding-top:50px}
.quote{position:absolute;left:300px;top:92px;width:610px;font-style:italic;font-size:12.5px;line-height:21px;color:var(--ink-soft)}
.quote-mark{position:absolute;font-family:Georgia,serif;font-size:42px;font-style:normal;color:var(--ink-soft);line-height:1}
.quote-mark--open{left:-24px;top:-6px}
.quote-mark--close{right:30px;bottom:-30px}
.quote-author{position:absolute;left:0;right:0;top:165px;font-size:13px;color:var(--ink)}

/* Footer */
.site-footer{height:257px;background:var(--footer-bg);border-top:1px solid var(--rule);position:relative}
.footer-col{position:absolute;top:41px;list-style:none}
.footer-col h3{font-family:"Raleway",sans-serif;font-size:15px;font-weight:500;margin-bottom:5px;color:var(--ink)}
.footer-col li{font-size:12.5px;line-height:21px;color:var(--ink-soft)}
.bottom-bar{height:57px;border-top:1px solid var(--rule);position:relative;background:var(--footer-bg)}
.copyright{position:absolute;left:163px;top:21px;font-size:11px;color:var(--ink-soft)}
.social{position:absolute;left:962px;top:20px;display:flex;gap:11px}
.social span{width:17px;height:17px;border-radius:50%;background:var(--social)}
</style>
</head>
<body>

<header class="site-header">
  <div class="brand"><span class="brand-mark"></span><span class="brand-name">Stir Your Shelves</span></div>
  <span class="member-link">Already Member</span>
  <span class="login-btn">Login</span>
</header>

<section class="hero">
  <div class="hero-photo" role="img" aria-label="Photo of a couple cooking together in a kitchen with a tablet, vegetables and oils on the counter"></div>
  <svg class="slider-arrow" style="left:92px" width="34" height="66" viewBox="0 0 34 66"><polyline points="32,2 2,33 32,64" fill="none" stroke="#fff" stroke-width="2"/></svg>
  <svg class="slider-arrow" style="left:1076px" width="34" height="66" viewBox="0 0 34 66"><polyline points="2,2 32,33 2,64" fill="none" stroke="#fff" stroke-width="2"/></svg>
  <div class="hero-panel">
    <p class="hero-kicker heading">REDISCOVER YOUR</p>
    <p class="hero-script">Cookbooks</p>
    <p class="hero-lead">Join a community of cookbook lovers &amp; discover that Stir Your Shelves is a great way to make better use of your own collection</p>
  </div>
</section>

<section class="features">
  <div class="feature feature--search">
    <div class="feature-photo" role="img" aria-label="Photo of a hand using a tablet next to fresh vegetables"></div>
    <h2 class="feature-title heading">Find any recipe from your own recipe</h2>
    <p class="feature-sub heading">Collection in seconds</p>
    <p class="feature-text">Stir Your Shelves has indexed over 1 million recipes – so now you can have a search engine to find all your recipes in your cookbooks, magazines &amp; favorite blogs</p>
  </div>
  <div class="feature feature--community">
    <div class="feature-photo" role="img" aria-label="Photo of a salad bowl with oil being poured"></div>
    <h2 class="feature-title heading">Connect with a community of</h2>
    <p class="feature-sub heading">like-minded enthusiasts</p>
    <p class="feature-text">Exchange recommendations with other members, discover new ideas &amp; read blogs written by culinary enthusiasts</p>
  </div>
</section>

<section class="join-band">
  <div class="join-photo" role="img" aria-label="Darkened photo of a family cooking together"></div>
  <div class="join-content">
    <h2 class="join-title heading">BECOME A MEAMBER AND START</h2>
    <p class="join-sub heading">ORGANIZING YOUR RECIPES</p>
    <span class="read-more">READ MORE</span>
  </div>
</section>

<section class="library">
  <div class="library-copy">
    <h2 class="library-title heading">Suggested New copy for Library recipe page</h2>
    <p class="library-sub heading">If this recipe is available online –<br>click on the link "View complete recipe" below</p>
    <p class="library-text">SYS is a recipe search engine for your personal collection. If there's no link, it means you need to own the book or magazine to see the complete recipe</p>
    <div class="library-actions">
      <span class="btn btn--primary">Find Out More</span>
      <span class="btn btn--dark">Join now and get started</span>
    </div>
  </div>
  <div class="library-photo" role="img" aria-label="Photo of a colourful buffet of dishes being served"></div>
</section>

<section class="testimonials">
  <h2 class="testimonials-title heading">TESTIMONIALS</h2>
  <svg class="slider-arrow" style="left:215px;top:105px" width="28" height="64" viewBox="0 0 28 64"><polyline points="26,2 2,32 26,62" fill="none" stroke="#555" stroke-width="1.5"/></svg>
  <svg class="slider-arrow" style="left:958px;top:105px" width="28" height="64" viewBox="0 0 28 64"><polyline points="2,2 26,32 2,62" fill="none" stroke="#555" stroke-width="1.5"/></svg>
  <blockquote class="quote">
    <span class="quote-mark quote-mark--open">“</span>
    Morbi diam mauris viverra in gravida eu mattis in ante Morbi eget arcu Morbi porta libero id ullamcorper non-ummy nibh ligula pulvinar metus eget consectetuer augue nisi quis lacus Ut ac mi quis lacus mollis aliquam Cura-bitur iaculis tempus eros Curabitur vel mi sit amet Mauris vel lacus vitae felis
    <span class="quote-mark quote-mark--close">”</span>
  </blockquote>
  <p class="quote-author">By Author Name, City Location</p>
</section>

<footer class="site-footer">
  <ul class="footer-col" style="left:158px">
    <h3>THE BEST RECIPES</h3>
    <li>Chicken</li><li>Fruit Tarts</li><li>Meatballs</li><li>Vegetarian Pasta</li><li>Chocolate Cakes</li><li>Gluten Free Baking</li>
  </ul>
  <ul class="footer-col" style="left:375px">
    <h3>THE BEST AUTHORS</h3>
    <li>Tomas Oberlin</li><li>Mark Bellweather</li><li>Dana Hollis</li><li>Annika Lindqvist</li><li>Clarisse Dumontel</li><li>Rosa Levin Barrow</li>
  </ul>
  <ul class="footer-col" style="left:584px">
    <h3>THE BEST COOKBOOKS</h3>
    <li>New Cookbooks</li><li>Most Popular Cookbooks</li><li>Indexed Baking Cookbooks</li><li>Indexed BBQ Cookbooks</li><li>Indexed Vegetarian Cookbooks</li><li>Index Kitchen Notebook</li>
  </ul>
  <ul class="footer-col" style="left:835px">
    <h3>STIR YOUR SHELVES</h3>
    <li>Quick Tour</li><li>Member Benefits</li><li>Getting Started</li><li>About Stir Your Shelves</li><li>Support Page</li><li>Email Preferences</li>
  </ul>
</footer>

<div class="bottom-bar">
  <p class="copyright">© 2015 Company Name &nbsp;All right reserved &nbsp;Term of Use</p>
  <div class="social" aria-label="Social links"><span></span><span></span><span></span></div>
</div>

</body>
</html>
```